Glass window Vinyl

We are in need of window vinyls for the building shown in the photos. The current vinyls will come down, and we will install the new signage created by this process. We need to advertise:

"Hartwell's Landing Pop Up Market"

Then, below that, it should say for rental inquiries call : 717.555.0193 with our logo which is attached along with our colors and brand guidelines. You may add more color to the Hartwells landing pop up market signage if appropriate. It should be large enough to be easily read from the road by those passing by.

```html
<!DOCTYPE html>
<html lang="en">
<head>
<meta charset="utf-8">
<title>Hartwell's Landing Pop Up Market – Window Vinyl</title>
<link rel="stylesheet" href="https://fonts.googleapis.com/css2?family=Cinzel:wght@400;600;700&display=swap">
<style>
  :root {
    --page-bg: #ffffff;
    --sign-teal: #013f50;
    --brand-gold: #b39a62;
    --ink-white: #ffffff;
  }
  html, body {
    margin: 0;
    padding: 0;
    width: 1200px;
    height: 806px;
    overflow: hidden;
    background: var(--page-bg);
  }
  .canvas {
    position: relative;
    width: 1200px;
    height: 806px;
  }
  .window-sign {
    position: absolute;
    left: 255px;
    top: 46px;
    width: 690px;
    height: 713px;
    background: var(--sign-teal);
    box-shadow: 4px 4px 6px rgba(0, 0, 0, 0.35);
    font-family: "Cinzel", serif;
    color: var(--ink-white);
    text-align: center;
  }
  .roof-band {
    position: absolute;
    inset: 0;
    width: 100%;
    height: 100%;
  }
  .market-title {
    position: absolute;
    left: 0;
    right: 0;
    top: 70px;
    margin: 0;
    font-weight: 700;
    line-height: 0.86;
    white-space: nowrap;
  }
  .market-title .line-one { display: block; font-size: 80px; }
  .market-title .line-two { display: block; font-size: 66px; }
  .market-title .line-three { display: block; font-size: 66px; }
  .brand-name {
    position: absolute;
    left: 0;
    right: 0;
    top: 478px;
    display: flex;
    justify-content: center;
    align-items: center;
    gap: 16px;
  }
  .brand-mark {
    width: 18px;
    height: 18px;
    background: var(--brand-gold);
  }
  .brand-wordmark {
    font-size: 27px;
    font-weight: 600;
    letter-spacing: 5px;
    color: var(--ink-white);
  }
  .rental-label {
    position: absolute;
    left: 0;
    right: 0;
    top: 588px;
    font-size: 19px;
    font-weight: 600;
    letter-spacing: 3px;
  }
  .rental-phone {
    position: absolute;
    left: 0;
    right: 0;
    top: 622px;
    font-size: 46px;
    font-weight: 600;
    color: var(--brand-gold);
    letter-spacing: 1px;
  }
</style>
</head>
<body>
<main class="canvas">
  <section class="window-sign">
    <svg class="roof-band" viewBox="0 0 808 835" preserveAspectRatio="none" aria-hidden="true">
      <polygon fill="var(--brand-gold)"
        points="0,465 192,377 615,377 808,465 808,500 615,405 192,405 0,500"/>
    </svg>
    <h1 class="market-title">
      <span class="line-one">"Hartwell's</span>
      <span class="line-two">Landing Pop Up</span>
      <span class="line-three">Market"</span>
    </h1>
    <div class="brand-name">
      <span class="brand-mark"></span>
      <span class="brand-wordmark">WILLOW CREST PROPERTIES</span>
    </div>
    <p class="rental-label" style="margin:0">for rental inquiries</p>
    <p class="rental-phone" style="margin:0">CALL : 717.555.0193</p>
  </section>
</main>
</body>
</html>
```